Business card design for sports medicine and athlete care clinic.

We need a bold, solid business card design for our practitioners to stand out. We treat overuse & sports-related injuries and provide post-operative rehabilitation. Our specialisations include chronic conditions, men’s health, nutrition & musculoskeletal disorders (MSDs). All brand collateral in terms of fonts, logo and colour palette to be provided.

Target Market(s)

Athletes (professional and amateur), sportspeople, predominantly male

Industry/Entity Type

Health And Wellness

Contact Information for Business Card

The front of the card should be white with dark blue text the back dark blue with white text. The logo should be top-left. The business name should be horizontal and right of the logo. The tagline should be directly below centred on the back of the card (see top-banner.png and bottom-banner.png)

Font styles to use
Sans Serif

Colors
0355a3
0293ce
3176b5
ffffff
85acd3

Requirements
Nice to have
• Diagonal and/or horizontal line elements between logo and practitioner details and/or bottom corner of card (see slide.png and tag-bg.png).

```html
<!DOCTYPE html>
<html lang="en">
<head>
<meta charset="utf-8">
<title>The Stride Collective – Business Card</title>
<link rel="stylesheet" href="https://fonts.googleapis.com/css2?family=Montserrat:wght@400;500;700;800&display=swap">
<style>
  :root {
    --backdrop: #8d8e8d;
    --card: #eeeef0;
    --navy: #0b0f4a;
    --brand-blue: #0355a3;
    --accent-blue: #0293ce;
    --name-blue: #0a78be;
    --relief-light: #f4f4f6;
    --relief-shade: #e4e4e8;
  }
  * { margin: 0; padding: 0; box-sizing: border-box; }
  html, body { width: 1200px; height: 1200px; overflow: hidden; }
  body {
    background: var(--backdrop);
    font-family: "Montserrat", sans-serif;
    color: var(--navy);
    position: relative;
  }
  .card {
    position: absolute;
    left: 209px;
    width: 796px;
    height: 441px;
    background: var(--card);
    overflow: hidden;
  }
  .card--front { top: 98px; }
  .card--back { top: 634px; }

  .runner-relief {
    position: absolute;
    left: 325px;
    top: 0;
    width: 471px;
    height: 441px;
    z-index: 0;
    background: radial-gradient(ellipse at 62% 48%, var(--relief-light) 0%, var(--relief-shade) 45%, var(--card) 75%);
  }

  .brand-mark {
    position: absolute;
    z-index: 1;
    border-radius: 50%;
    background: var(--accent-blue);
  }
  .brand-name {
    position: absolute;
    z-index: 1;
    font-weight: 800;
    color: var(--navy);
    white-space: nowrap;
    letter-spacing: 0.5px;
  }
  .brand-tagline {
    position: absolute;
    z-index: 1;
    font-weight: 500;
    color: var(--accent-blue);
    white-space: nowrap;
    letter-spacing: 0.8px;
  }

  .card--front .brand-mark { left: 50px; top: 52px; width: 52px; height: 52px; }
  .card--front .brand-name { left: 129px; top: 40px; font-size: 27px; }
  .card--front .brand-tagline { left: 130px; top: 80px; font-size: 13px; }

  .person { position: absolute; z-index: 1; left: 43px; top: 190px; }
  .person__name { font-size: 26px; font-weight: 700; color: var(--name-blue); line-height: 1.1; }
  .person__role { font-size: 17px; font-weight: 400; color: var(--navy); margin-top: 2px; }

  .contact-list { position: absolute; z-index: 1; left: 42px; top: 303px; list-style: none; }
  .contact-list li {
    display: flex; align-items: center; gap: 6px;
    height: 25px; font-size: 17px; color: var(--navy);
  }
  .contact-list svg { width: 15px; height: 15px; flex: none; }

  .card--back .brand-mark { left: 150px; top: 185px; width: 80px; height: 80px; }
  .card--back .brand-name { left: 258px; top: 180px; font-size: 40px; }
  .card--back .brand-tagline { left: 260px; top: 234px; font-size: 19px; }
</style>
</head>
<body>

<section class="card card--front">
  <div class="runner-relief" role="img" aria-label="Blind-embossed sprinting athlete figure"></div>

  <span class="brand-mark"></span>
  <div class="brand-name">The Stride Collective</div>
  <div class="brand-tagline">Sports medicine and athlete care</div>

  <div class="person">
    <div class="person__name">Lukas Fenner</div>
    <div class="person__role">Director</div>
  </div>

  <ul class="contact-list">
    <li>
      <svg viewBox="0 0 16 16" aria-hidden="true"><rect x="3" y="1" width="10" height="14" rx="1.5" fill="none" stroke="#0a78be" stroke-width="1.6"/><circle cx="8" cy="12.5" r="0.9" fill="#0a78be"/></svg>
      +41 70 555 01 23
    </li>
    <li>
      <svg viewBox="0 0 16 16" aria-hidden="true"><path d="M3 2.5l2.5-.5 1.5 3.5-1.6 1.2a8 8 0 0 0 3.9 3.9l1.2-1.6 3.5 1.5-.5 2.5C9 13.5 2.5 7 3 2.5z" fill="#0a78be"/><path d="M9.5 2.5a4 4 0 0 1 4 4M9.5 0.8a5.7 5.7 0 0 1 5.7 5.7" fill="none" stroke="#0a78be" stroke-width="1.1"/></svg>
      +43 660 555 04 876
    </li>
    <li>
      <svg viewBox="0 0 16 16" aria-hidden="true"><rect x="1" y="3" width="14" height="10" rx="1" fill="#0a78be"/><path d="M1.5 3.8L8 9l6.5-5.2" fill="none" stroke="#eeeef0" stroke-width="1.2"/></svg>
      hello@stridecollective.com
    </li>
    <li>
      <svg viewBox="0 0 16 16" aria-hidden="true"><circle cx="8" cy="8" r="6.8" fill="none" stroke="#0a78be" stroke-width="1.4"/><ellipse cx="8" cy="8" rx="3" ry="6.8" fill="none" stroke="#0a78be" stroke-width="1.1"/><path d="M1.5 8h13" stroke="#0a78be" stroke-width="1.1"/></svg>
      www.stridecollective.com
    </li>
  </ul>
</section>

<section class="card card--back">
  <span class="brand-mark"></span>
  <div class="brand-name">The Stride Collective</div>
  <div class="brand-tagline">Sports medicine and athlete care</div>
</section>

</body>
</html>
```